Buff & Gleam

polished concrete and epoxy coatings flooring company

Target Market(s)

Industrial commercial

Industry/Entity Type

Industrial flooring contractor

Contact Information for Business Card

POLISHED CONCRETE • EPOXY COATING • TERRAZZO RESTORATION • SHOT BLASTING • SURFACE PREPARATION • JOINT FILLING • TILE/ CARPET /GLUE REMOVAL

Colors
0054AA
0677BA
7BADD7
CADEEF
E8F1F8

Requirements
Must have
• email buffandgleamfloors@mailbrook.example Address 47215 Tallowmere Rd, Fraser, MI 48093. Name Ray Tulvin. Services Polished concrete- Epoxy Coatings- Terrazzo restoration-surface preparation- safety striping- joint filling- tile/ carpet/ glue removal phone number 586-700-3926 email buffandgleamfloors.example
Nice to have
• Instagram Facebook logo maybe smaller in the corner

```html
<!DOCTYPE html>
<html lang="en">
<head>
<meta charset="utf-8">
<title>Buff &amp; Gleam — Business Card</title>
<link href="https://fonts.googleapis.com/css2?family=Poppins:wght@400;600;700&family=Oswald:wght@500&display=swap" rel="stylesheet">
<style>
  :root {
    --page: #ffffff;
    --card: #a3cfcc;
    --card-light: #b9dcd9;
    --ink: #263638;
    --icon: #3f6664;
  }
  * { margin: 0; padding: 0; box-sizing: border-box; }
  html, body { width: 1200px; height: 1200px; overflow: hidden; background: var(--page); }
  body { position: relative; font-family: "Poppins", sans-serif; color: var(--ink); }

  .card {
    position: absolute;
    left: 184px;
    width: 839px;
    height: 480px;
    background: var(--card);
    overflow: hidden;
  }
  .card--front { top: 119px; }
  .card--back { top: 608px; }

  .contour-field { position: absolute; inset: 0; width: 100%; height: 100%; }

  .brand { position: absolute; text-align: center; }
  .brand__name {
    font-family: "Poppins", sans-serif;
    font-weight: 600;
    color: var(--ink);
    line-height: 1.05;
    letter-spacing: 0.02em;
  }
  .brand__tagline {
    font-family: "Oswald", sans-serif;
    font-weight: 500;
    color: var(--ink);
    letter-spacing: 0.06em;
    text-transform: uppercase;
  }

  .card--front .brand { left: 0; right: 0; top: 130px; }
  .card--front .brand__name { font-size: 66px; }
  .card--front .brand__tagline { font-size: 20px; margin-top: 22px; }

  .services {
    position: absolute;
    left: 0; right: 0; top: 326px;
    text-align: center;
    font-weight: 600;
    font-size: 13.2px;
    line-height: 16px;
  }

  .card--back .brand { left: 140px; width: 178px; top: 190px; }
  .card--back .brand__name { font-size: 38px; }
  .card--back .brand__tagline { font-size: 11.5px; margin-top: 10px; letter-spacing: 0.03em; white-space: nowrap; }

  .contact { position: absolute; left: 452px; top: 122px; max-width: 370px; }
  .contact__name { margin-left: 26px; font-weight: 700; font-size: 24px; line-height: 34px; }
  .contact__list { list-style: none; margin-top: 30px; }
  .contact__item {
    display: flex; align-items: center; gap: 12px;
    font-size: 15.5px; line-height: 31px; white-space: nowrap;
  }
  .contact__icon { width: 14px; height: 14px; flex: none; }
  .contact__address { margin: 28px 0 0 26px; font-size: 15.5px; line-height: 20px; }
</style>
</head>
<body>

<section class="card card--front">
  <svg class="contour-field" viewBox="0 0 839 480" role="img" aria-label="Topographic contour line pattern sweeping diagonally across the left of the card">
    <defs>
      <linearGradient id="frontWash" x1="0" y1="0" x2="1" y2="0">
        <stop offset="0" stop-color="#b9dcd9"/>
        <stop offset="1" stop-color="#a3cfcc"/>
      </linearGradient>
    </defs>
    <path d="M0 0 H290 C230 130 200 240 170 330 C140 420 100 460 40 480 H0 Z" fill="url(#frontWash)"/>
  </svg>
  <div class="brand">
    <div class="brand__name">Buff &amp; Gleam</div>
    <div class="brand__tagline">Innovative Concrete Flooring</div>
  </div>
  <p class="services">
    Polished Concrete-Epoxy Coatings-Terrazzo Restoration-Surface Preparation<br>
    Safety Striping-Joint Filling-Tile/Carpet/Glue Removal
  </p>
</section>

<section class="card card--back">
  <svg class="contour-field" viewBox="0 0 839 480" role="img" aria-label="Topographic contour line pattern flowing across the card in wide waves">
    <defs>
      <linearGradient id="backWash" x1="0" y1="0" x2="1" y2="1">
        <stop offset="0" stop-color="#a3cfcc"/>
        <stop offset="0.5" stop-color="#b9dcd9"/>
        <stop offset="1" stop-color="#a3cfcc"/>
      </linearGradient>
    </defs>
    <path d="M300 0 C200 90 150 170 200 260 C260 330 440 380 610 480 H839 V0 Z" fill="url(#backWash)" opacity="0.7"/>
  </svg>
  <div class="brand">
    <div class="brand__name">Buff &amp; Gleam</div>
    <div class="brand__tagline">Innovative Concrete Flooring</div>
  </div>
  <div class="contact">
    <h1 class="contact__name">Ray Tulvin</h1>
    <ul class="contact__list">
      <li class="contact__item">
        <svg class="contact__icon" viewBox="0 0 16 16" fill="none" stroke="var(--icon)" stroke-width="1.2"><circle cx="8" cy="8" r="6.5"/><ellipse cx="8" cy="8" rx="3" ry="6.5"/><path d="M1.5 8h13M2.5 4.5h11M2.5 11.5h11"/></svg>
        <span>buffandgleamfloors.example</span>
      </li>
      <li class="contact__item">
        <svg class="contact__icon" viewBox="0 0 16 16" fill="none" stroke="var(--icon)" stroke-width="1.2"><rect x="1.5" y="3" width="13" height="10" rx="1.5"/><path d="M2 4l6 5 6-5"/></svg>
        <span>buffandgleamfloors@mailbrook.example</span>
      </li>
      <li class="contact__item">
        <svg class="contact__icon" viewBox="0 0 16 16" fill="none" stroke="var(--icon)" stroke-width="1.2"><path d="M3 1.8l2.4-.3 1.5 3.4-1.6 1.2c.8 1.8 2.1 3.1 3.9 3.9l1.2-1.6 3.4 1.5-.3 2.4c-.1.6-.6 1-1.2 1C6.6 13.2 2.8 9.4 2 3c0-.6.4-1.1 1-1.2z"/></svg>
        <span>586-700-3926</span>
      </li>
    </ul>
    <p class="contact__address">47215 Tallowmere Rd,<br>Fraser, MI 48093.</p>
  </div>
</section>

</body>
</html>
```